Interior Design & consultancy firm requires a new business card design that is a little bit funky bu

Kestrova Design Services is a leading strategic design practice specialising in the development and implementation of strategies and design solutions for commercial workplaces across a wide variety of industries.

The company has over twenty years experience in the strategic design, development and construction of innovative and efficient workplace environments for the commercial, corporate and industrial sectors.

We believe good design and efficient workspaces can transform companies, improve people’s lives and increase productivity.

Target Market(s)

My clients are mainly Government or corporate clients wanting to create a statement with their office fitout & new furniture that reflects their corporate identity

Industry/Entity Type

Construction

Font styles to use
Sans Serif

Colors
add136

Requirements
Must have
• The business card must be easy to read, simple & highlight my name & mobile phone number
Should not have
• I do not want the card to be fussy, feature too many colours or look to busy.

```html
<!DOCTYPE html>
<html lang="en">
<head>
<meta charset="utf-8">
<title>Kestrova Design Services – Business Cards</title>
<link href="https://fonts.googleapis.com/css2?family=Open+Sans:wght@400;600;700&display=swap" rel="stylesheet">
<style>
  :root {
    --page-bg: #e9e7e3;
    --card-dark-top: #2f3032;
    --card-dark-bottom: #4a4b4e;
    --card-light: #ffffff;
    --card-light-shade: #eceded;
    --brand-blue: #1f8fd0;
    --brand-blue-light: #3fb4e6;
    --strip-grey: #3b3c3e;
    --text-light: #e6e6e6;
    --text-grey: #6a6a6a;
    --text-dark: #3a3a3a;
  }
  * { box-sizing: border-box; margin: 0; padding: 0; }
  html, body {
    width: 1200px; height: 1023px; overflow: hidden;
    background: var(--page-bg);
    font-family: "Open Sans", Arial, sans-serif;
  }
  .stage {
    width: 1200px; height: 1023px;
    display: flex; align-items: center; justify-content: center; gap: 44px;
  }
  .card {
    width: 530px; height: 324px; position: relative; overflow: hidden;
    border-radius: 4px;
    box-shadow: 0 10px 28px rgba(0,0,0,.18);
  }
  /* Front card */
  .card--front {
    background: linear-gradient(160deg, var(--card-dark-top), var(--card-dark-bottom));
    color: var(--text-light);
  }
  .front__brand {
    position: absolute; left: 50px; top: 96px;
    display: flex; align-items: center; gap: 16px;
  }
  .brand-dot {
    width: 22px; height: 22px; border-radius: 50%;
    background: var(--brand-blue-light); flex: none;
  }
  .front__name {
    font-weight: 700; font-size: 27px; color: var(--brand-blue-light);
    letter-spacing: .2px; line-height: 1.15;
  }
  .front__tagline {
    position: absolute; left: 50px; right: 44px; top: 196px;
    font-size: 12.5px; line-height: 1.55; color: var(--text-light);
  }
  /* Back card */
  .card--back {
    background: linear-gradient(135deg, var(--card-light) 45%, var(--card-light-shade));
  }
  .back__strip {
    position: absolute; left: 0; top: 0; bottom: 0; width: 22px;
    display: flex; flex-direction: column;
  }
  .back__strip-top { flex: 0 0 62%; background: var(--strip-grey); }
  .back__strip-bottom { flex: 1; background: var(--brand-blue); }
  .back__brand {
    position: absolute; right: 34px; top: 42px;
    display: flex; align-items: center; gap: 12px;
  }
  .back__brand .front__name { font-size: 20px; color: var(--brand-blue); text-align: right; }
  .back__brand .brand-dot { background: var(--brand-blue); width: 16px; height: 16px; }
  .person {
    position: absolute; left: 50px; top: 48px;
  }
  .person__name {
    font-weight: 700; font-size: 17px; color: var(--brand-blue);
    letter-spacing: .6px; text-transform: uppercase;
  }
  .person__role, .person__degree {
    font-size: 11.5px; color: var(--text-grey); margin-top: 5px;
  }
  .person__role { margin-top: 8px; }
  .contact {
    position: absolute; left: 50px; bottom: 60px;
    display: flex; align-items: center; gap: 10px;
    font-size: 13px; color: var(--text-grey); letter-spacing: 1px;
  }
  .contact svg { width: 14px; height: 18px; }
</style>
</head>
<body>
<main class="stage">
  <section class="card card--front" aria-label="Card front">
    <div class="front__brand">
      <span class="brand-dot"></span>
      <div class="front__name">Kestrova Design<br>Services Pty Ltd</div>
    </div>
    <p class="front__tagline">We are design practice specialising in the development and implementation of strategies and design solutions for commercial workplaces</p>
  </section>

  <section class="card card--back" aria-label="Card back">
    <div class="back__strip">
      <div class="back__strip-top"></div>
      <div class="back__strip-bottom"></div>
    </div>
    <div class="person">
      <h1 class="person__name">Marla Henshaw</h1>
      <p class="person__role">Director / Senior Interior Designer</p>
      <p class="person__degree">Bachelor of Arts in Interior Design</p>
    </div>
    <div class="back__brand">
      <div class="front__name">Kestrova Design<br>Services Pty Ltd</div>
      <span class="brand-dot"></span>
    </div>
    <div class="contact">
      <svg viewBox="0 0 14 18" aria-hidden="true">
        <rect x="1" y="1" width="12" height="16" rx="2" fill="none" stroke="var(--brand-blue)" stroke-width="2"/>
        <rect x="4" y="4" width="6" height="7" fill="var(--brand-blue)"/>
      </svg>
      <span>0400 517 283</span>
    </div>
  </section>
</main>
</body>
</html>
```